business cards/stationary for construction company
FERN HOLLOW BUILDERS, LLC
Simple
GENERAL CONTRACTORS
PO Box 48315
Bozeman, MT 59284
fhbuilders.llc@postvale.net
We want two names and #'s on the cards:
Dana Whitcombe 702.555.0148 & Ryan Pettigrew 702.555.0193
new logo.. please take a look

```html
<!DOCTYPE html>
<html lang="en">
<head>
<meta charset="utf-8">
<title>Fern Hollow Builders, LLC — Business Cards</title>
<link href="https://fonts.googleapis.com/css2?family=Cormorant+Garamond:wght@400;500&family=Cinzel:wght@400&display=swap" rel="stylesheet">
<style>
  :root {
    --backdrop: #e6e1da;
    --card: #ffffff;
    --ink: #3a4350;
    --ink-soft: #6d7786;
    --slate: #9aa7b9;
    --slate-light: #c6cfdb;
    --rule: #b9c2ce;
  }
  * { margin: 0; padding: 0; box-sizing: border-box; }
  html, body {
    width: 1200px; height: 629px; overflow: hidden;
    background: var(--backdrop);
  }
  .sheet {
    position: relative; width: 1200px; height: 629px;
    display: flex; align-items: center; justify-content: center; gap: 60px;
  }
  .card {
    position: relative; width: 500px; height: 286px;
    background: var(--card);
    box-shadow: 0 6px 18px rgba(60, 50, 40, 0.18);
    overflow: hidden;
  }
  .brand {
    display: flex; align-items: center; gap: 12px;
    font-family: "Cormorant Garamond", serif; font-weight: 500;
    color: var(--ink);
  }
  .brand-mark {
    width: 18px; height: 18px; background: var(--slate); flex: none;
  }
  .card-front .brand {
    position: absolute; left: 0; right: 0; top: 0; bottom: 0;
    justify-content: center; font-size: 30px;
  }
  .card-back .brand {
    position: absolute; left: 34px; top: 58px; font-size: 21px;
  }
  .card-back .brand-mark { width: 13px; height: 13px; }
  .contact {
    position: absolute; left: 292px; top: 40px;
    padding-left: 16px; border-left: 1px solid var(--rule);
    font-family: "Cormorant Garamond", serif; font-size: 12.5px; line-height: 1.55;
    color: var(--ink-soft); list-style: none;
  }
  .contact li { display: flex; align-items: center; gap: 7px; }
  .contact svg { width: 10px; height: 10px; flex: none; }
  .company {
    position: absolute; left: 34px; top: 176px;
    font-family: "Cinzel", serif; color: var(--ink-soft);
    letter-spacing: 0.14em;
  }
  .company-name { font-size: 11px; }
  .company-trade { font-size: 9px; margin-top: 4px; letter-spacing: 0.22em; }
  .band {
    position: absolute; left: 0; right: 0; bottom: 30px; height: 26px;
    background: var(--slate);
    border-top: 2px solid var(--slate-light);
    display: flex; align-items: center; justify-content: flex-end;
    padding-right: 34px;
    font-family: "Cinzel", serif; font-size: 10px; letter-spacing: 0.35em;
    color: #ffffff;
  }
</style>
</head>
<body>
<main class="sheet">
  <section class="card card-front" aria-label="Card front">
    <div class="brand"><span class="brand-mark"></span>Fern Hollow Builders, LLC</div>
  </section>

  <section class="card card-back" aria-label="Card back">
    <div class="brand"><span class="brand-mark"></span>Fern Hollow Builders, LLC</div>
    <ul class="contact">
      <li><svg viewBox="0 0 10 10"><path d="M2 1h2l1 2-1.2 1a5 5 0 0 0 2.2 2.2L7 5l2 1v2a1 1 0 0 1-1 1A7 7 0 0 1 1 2a1 1 0 0 1 1-1z" fill="#9aa7b9"/></svg>Dana Whitcombe 702.555.0148</li>
      <li><svg viewBox="0 0 10 10"><path d="M2 1h2l1 2-1.2 1a5 5 0 0 0 2.2 2.2L7 5l2 1v2a1 1 0 0 1-1 1A7 7 0 0 1 1 2a1 1 0 0 1 1-1z" fill="#9aa7b9"/></svg>Ryan Pettigrew 702.555.0193</li>
      <li><svg viewBox="0 0 10 10"><path d="M5 0.5a3.3 3.3 0 0 0-3.3 3.3C1.7 6.3 5 9.5 5 9.5s3.3-3.2 3.3-5.7A3.3 3.3 0 0 0 5 0.5zm0 4.6a1.3 1.3 0 1 1 0-2.6 1.3 1.3 0 0 1 0 2.6z" fill="#9aa7b9"/></svg>PO Box 48315</li>
      <li><svg viewBox="0 0 10 10"></svg>Bozeman, MT 59284</li>
      <li><svg viewBox="0 0 10 10"><rect x="0.5" y="2" width="9" height="6" fill="none" stroke="#9aa7b9"/><path d="M0.5 2 5 5.5 9.5 2" fill="none" stroke="#9aa7b9"/></svg>fhbuilders.llc@postvale.net</li>
    </ul>
    <div class="company">
      <p class="company-name">FERN HOLLOW BUILDERS, LLC</p>
      <p class="company-trade">GENERAL CONTRACTORS</p>
    </div>
    <div class="band">www.fhbuilders.net</div>
  </section>
</main>
</body>
</html>
```